Design a modern, premium front panel for a stand-up pouch

Design a modern, premium front for a stand-up pouch for VELUTRA. Product is for Urine/vomit/runny stool incidents indoors; quick cleanups before smell sets; nighttime/elderly pet accidents; travel/car mishaps.

It must instantly show it’s for dogs & cats and include three small step icons with labels: Sprinkle → Wait 1–5 min → Sweep. Front copy to include: VELUTRA, descriptor “Mineral Instant Absorber – for Dogs & Cats”, one benefits line “Fragrance-Free • 100 % Mineral • Odor-Binding • Low-Dust

Goal: clear who/what/how in under 3 seconds
Deliverables: AI/PDF + a pouch mockup;

Target Market(s)

• Dog & cat households in apartments/homes; new pet parents, senior pets, multi-pet homes. • Cleanliness & odor-sensitive buyers (allergies/asthma, fragrance-free preference). • Surfaces at risk: carpets/rugs, sofas, mattresses, car interiors.

Industry/Entity Type

Pet e-commerce and retail

Font styles to use
Other font styles liked:
• like attached images

Requirements
Nice to have
• light background, eco friendly

```html
<!DOCTYPE html>
<html lang="en">
<head>
<meta charset="utf-8">
<title>VELUTRA – Mineral Instant Absorber pouch front</title>
<link href="https://fonts.googleapis.com/css2?family=Jost:wght@200&family=Montserrat:wght@400;600;700&display=swap" rel="stylesheet">
<style>
  :root{
    --bg:#ffffff;
    --panel:#ffffff;
    --frame:#5a5a55;
    --logo:#b9b2a6;
    --ink-dark:#4f5147;
    --ink-olive:#7b7e6c;
    --ink-grey:#6a6a64;
    --pill:#8a8d75;
    --rule:#5d5f52;
    --paw:#9a9d86;
    --silhouette:#4b4d3d;
    --wave-back:#c6c7b7;
    --wave-front:#a8aa91;
  }
  *{margin:0;padding:0;box-sizing:border-box}
  html,body{width:1200px;height:1200px;overflow:hidden;background:var(--bg)}
  .canvas{position:relative;width:1200px;height:1200px}
  .pouch-front{
    position:absolute;left:240px;top:62px;width:677px;height:1011px;
    transform:scale(1.0635);transform-origin:top left;
    background:var(--panel);border:1px solid var(--frame);overflow:hidden;
    font-family:'Montserrat',sans-serif;
  }
  .centered{position:absolute;left:0;right:0;text-align:center;line-height:1}
  .brand-name{top:230px;font-family:'Jost',sans-serif;font-weight:200;font-size:72px;letter-spacing:10px;color:var(--logo);padding-left:10px}
  .descriptor{top:339px;font-weight:600;font-size:19px;letter-spacing:1.6px;color:var(--ink-dark)}
  .headline{top:368px;font-weight:700;font-size:41px;letter-spacing:1.5px;color:var(--ink-olive)}
  .benefits{top:411px;font-weight:400;font-size:18px;letter-spacing:1.6px;color:var(--ink-grey)}
  .pet-art{position:absolute;left:232px;top:475px;width:220px;height:182px;border-radius:40px 40px 12px 12px;
    background:linear-gradient(135deg,var(--silhouette),#5d604c)}
  .audience-pill{position:absolute;left:177px;top:683px;width:329px;height:28px;border-radius:14px;background:var(--pill);
    color:#fff;font-weight:600;font-size:19px;letter-spacing:2px;text-align:center;line-height:29px}
  .divider{position:absolute;left:171px;top:736px;width:342px;height:3px;background:var(--rule)}
  .step{position:absolute;top:762px;width:120px;margin-left:-60px;text-align:center}
  .step svg{display:block;margin:0 auto;width:44px;height:44px}
  .step-title{margin-top:8px;font-weight:700;font-size:17px;letter-spacing:1.4px;color:var(--ink-dark);line-height:1}
  .step-sub{margin-top:3px;font-weight:400;font-size:14px;letter-spacing:1.2px;color:var(--ink-grey);line-height:1}
  .paw{position:absolute;border-radius:50%;background:var(--paw)}
  .waves{position:absolute;left:0;bottom:0;width:677px;height:160px}
  .claim{top:889px;font-weight:400;font-size:17px;letter-spacing:1.8px;color:var(--ink-grey)}
</style>
</head>
<body>
<div class="canvas">
  <section class="pouch-front">
    <span class="paw" style="left:201px;top:126px;width:18px;height:18px" aria-hidden="true"></span>
    <span class="paw" style="left:568px;top:218px;width:30px;height:30px" aria-hidden="true"></span>
    <span class="paw" style="left:97px;top:274px;width:26px;height:26px" aria-hidden="true"></span>
    <span class="paw" style="left:131px;top:510px;width:24px;height:24px" aria-hidden="true"></span>
    <span class="paw" style="left:36px;top:549px;width:24px;height:24px" aria-hidden="true"></span>
    <span class="paw" style="left:547px;top:544px;width:26px;height:26px" aria-hidden="true"></span>
    <span class="paw" style="left:87px;top:784px;width:32px;height:32px" aria-hidden="true"></span>
    <span class="paw" style="left:596px;top:828px;width:20px;height:20px" aria-hidden="true"></span>

    <div class="centered brand-name">VELUTRA</div>
    <div class="centered descriptor">MINERAL INSTANT ABSORBER</div>
    <div class="centered headline">100 % MINERAL</div>
    <div class="centered benefits">ODOR-BINDING · LOW-DUST</div>

    <div class="pet-art" role="img" aria-label="Silhouette illustration of a cat and a dog standing together"></div>

    <div class="audience-pill">FOR DOGS &amp; CATS</div>
    <div class="divider"></div>

    <div class="step" style="left:193px">
      <svg viewBox="0 0 44 44" aria-hidden="true">
        <g fill="var(--ink-dark)"><circle cx="20" cy="4" r="1.2"/><circle cx="24" cy="6" r="1.2"/><circle cx="21" cy="9" r="1.2"/><circle cx="25" cy="12" r="1.2"/><circle cx="20" cy="14" r="1.2"/><circle cx="23" cy="18" r="1.2"/></g>
        <path d="M4 38 L14 28 Q22 20 30 28 L40 38 Z" fill="var(--ink-dark)"/>
      </svg>
      <div class="step-title">SPRINKLE</div>
      <div class="step-sub">MINERAL</div>
    </div>
    <div class="step" style="left:341px">
      <svg viewBox="0 0 44 44" aria-hidden="true" fill="none" stroke="var(--ink-dark)" stroke-width="2.6" stroke-linecap="round">
        <path d="M36 22 A15 15 0 1 1 30 10"/>
        <path d="M30 10 L31 4 M30 10 L36 11"/>
        <path d="M21 13 V23 L27 27"/>
      </svg>
      <div class="step-title">WAIT</div>
      <div class="step-sub">1–5 MINS</div>
    </div>
    <div class="step" style="left:475px">
      <svg viewBox="0 0 44 44" aria-hidden="true">
        <path d="M36 4 L24 22" stroke="var(--ink-dark)" stroke-width="2.6" stroke-linecap="round"/>
        <path d="M20 19 L28 25 L20 38 L8 30 Z" fill="var(--ink-dark)"/>
        <path d="M10 8 l1.5 3 3 1.5 -3 1.5 -1.5 3 -1.5 -3 -3 -1.5 3 -1.5z M38 30 l1 2 2 1 -2 1 -1 2 -1 -2 -2 -1 2 -1z" fill="var(--ink-dark)"/>
      </svg>
      <div class="step-title">SWEEP</div>
      <div class="step-sub">CLEAN</div>
    </div>

    <svg class="waves" viewBox="0 0 677 160" preserveAspectRatio="none" aria-hidden="true">
      <path d="M0 12 Q120 -14 260 30 Q420 78 540 30 Q620 0 677 14 L677 160 L0 160 Z" fill="var(--wave-back)"/>
      <path d="M0 54 Q110 40 240 78 Q360 110 460 62 Q560 28 677 40 L677 160 L0 160 Z" fill="var(--wave-front)"/>
    </svg>
    <div class="centered claim">FRAGRANCE-FREE</div>
  </section>
</div>
</body>
</html>
```